Mesa Brew Circle - A Monthly Subscription Coffee Club - Shopify Website Design

A monthly subscription company. Need a Shopify Website Design and uploaded to fully work with Tidal Recurrings.

Please look at these sites for examples as well as the images I enclosed.

https://www.sipvantor.example/
https://grindcrate.example/
https://www.plattermint.example/
https://www.globalnibblory.example/

Number of Pages Required

1 page

```html
<!DOCTYPE html>
<html lang="en">
<head>
<meta charset="utf-8">
<title>Mesa Brew Circle – Monthly Coffee Subscription</title>
<link rel="stylesheet" href="https://fonts.googleapis.com/css2?family=Marcellus&family=Poppins:wght@300;400;500&display=swap">
<style>
:root{
  --ink:#1c1a19;
  --dark:#141211;
  --sand:#dccbb6;
  --sand-dark:#c9b497;
  --text:#5b5552;
  --muted:#8b8480;
  --white:#ffffff;
}
*{box-sizing:border-box;margin:0;padding:0}
html,body{width:1200px;height:4928px;overflow:hidden}
body{position:relative;background:var(--white);font-family:"Poppins",sans-serif;color:var(--text);font-size:13px;line-height:1.7}
.abs{position:absolute}
.btn{display:inline-block;background:var(--sand);color:var(--ink);font-size:11px;letter-spacing:.5px;text-transform:uppercase;padding:9px 22px;font-weight:500}
.section-title{font-family:"Marcellus",serif;font-weight:400;font-size:40px;color:var(--ink);text-align:center;width:1200px;left:0}
.title-rule{width:50px;height:2px;background:var(--ink);left:575px}

/* hero */
.hero{top:0;left:0;width:1200px;height:880px}
.hero-photo{top:0;left:0;width:1200px;height:880px;background:linear-gradient(105deg,#2a1c14 0%,#3b2a1f 40%,#6b5444 60%,#bfb2a5 80%,#e2dbd3 100%)}
.topbar{top:22px;left:110px;color:var(--white);font-size:12px;display:flex;align-items:center;gap:10px}
.nav{top:70px;left:110px;width:980px;height:40px;display:flex;align-items:center;color:var(--white);font-size:12px;text-transform:uppercase}
.nav a{color:inherit;text-decoration:none;margin-right:80px}
.logo{font-family:"Marcellus",serif;text-transform:none;font-size:26px;line-height:1;text-align:center;margin-right:80px}
.nav-icons{margin-left:auto;display:flex;gap:18px}
.hero h1{top:262px;left:110px;font-family:"Marcellus",serif;font-weight:400;color:var(--white);font-size:52px;line-height:1.25}
.hero p{top:400px;left:110px;width:440px;color:#eee;font-size:13px}
.hero .btn{top:480px;left:110px}
.tear{left:0;width:1200px}

/* about */
.about-text{top:960px;left:170px;width:860px;text-align:center;font-size:13px}

/* steps */
.step{top:1540px;width:310px;height:390px;background:var(--white);border-radius:14px;box-shadow:0 8px 30px rgba(0,0,0,.1);text-align:center;padding:50px 30px}
.step h3{font-family:"Marcellus",serif;font-weight:400;font-size:22px;color:var(--ink);line-height:1.25;margin-top:20px}
.step .rule{width:50px;height:2px;background:var(--ink);margin:14px auto 16px}

/* products */
.product{top:2250px;width:300px;text-align:center}
.product .shot{height:330px;background:linear-gradient(#f6f4f2,#fff);display:flex;align-items:center;justify-content:center}
.bag{width:110px;height:290px}
.product h4{font-family:"Marcellus",serif;font-weight:400;font-size:20px;color:var(--ink);margin-top:30px}
.product span{font-size:13px;color:var(--muted)}

/* banner */
.banner{top:2730px;left:0;width:1200px;height:480px;background:linear-gradient(100deg,#1d140f 0%,#3d2a1f 40%,#5a4334 55%,#2b1e16 75%,#120c09 100%)}
.banner h2{top:140px;left:0;width:1200px;text-align:center;font-family:"Marcellus",serif;font-weight:400;color:var(--white);font-size:42px;line-height:1.25}
.banner p{top:258px;left:0;width:1200px;text-align:center;color:var(--white);font-size:22px}
.banner .btn{top:336px;left:540px}

/* blogs */
.blog{top:3432px;width:310px;height:440px;background:var(--white);border-radius:14px;box-shadow:0 8px 30px rgba(0,0,0,.1);overflow:hidden}
.blog .shot{height:190px}
.blog .body{padding:22px}
.blog h4{font-family:"Marcellus",serif;font-weight:400;font-size:22px;color:var(--ink)}
.blog .date{font-size:11px;color:var(--muted);display:block;margin-bottom:10px}
.blog .more{display:block;margin-top:14px;font-size:11px;color:var(--sand-dark);text-transform:uppercase}
.partner{top:4050px;width:130px;height:130px;border-radius:50%;background:#ececec}

/* footer */
.footer{top:4300px;left:0;width:1200px;height:628px;background:var(--dark);color:#cfc9c4}
.foot-logo{top:200px;left:110px;font-family:"Marcellus",serif;color:var(--white);font-size:44px;line-height:1.05}
.foot-about{top:330px;left:110px;width:410px;font-size:13px}
.foot-read{top:405px;left:110px;color:var(--white);font-size:12px;text-decoration:underline}
.signup{top:470px;left:110px;display:flex}
.signup .field{width:260px;height:50px;background:var(--white);color:var(--ink);font-size:12px;padding:16px 20px}
.signup .btn{height:50px;padding:17px 26px}
.foot-h{font-family:"Marcellus",serif;font-weight:400;color:var(--white);font-size:36px}
.foot-list{font-size:13px;color:#cfc9c4;line-height:1.65}
.copy{top:590px;left:110px;font-size:11px;color:#bbb}
.social{top:592px;left:1000px;display:flex;gap:14px}
.social i{width:14px;height:14px;border-radius:50%;background:#bbb;display:block}
</style>
</head>
<body>

<section class="hero abs">
  <div class="hero-photo abs" role="img" aria-label="Photo of a cup of black coffee on a saucer with roasted beans around it"></div>
  <div class="topbar abs">
    <svg width="14" height="14" viewBox="0 0 24 24" fill="#fff"><path d="M6.6 10.8a15 15 0 0 0 6.6 6.6l2.2-2.2c.3-.3.7-.4 1-.2 1.1.4 2.3.6 3.6.6.6 0 1 .4 1 1V20c0 .6-.4 1-1 1A17 17 0 0 1 3 4c0-.6.4-1 1-1h3.5c.6 0 1 .4 1 1 0 1.3.2 2.5.6 3.6.1.3 0 .7-.2 1z"/></svg>
    <span>Call us : (+00) 012 345 6789</span>
  </div>
  <nav class="nav abs">
    <a href="#">About Us</a><a href="#">Shop</a><a href="#">Subscribe</a>
    <div class="logo">Mesa Brew<br>Circle</div>
    <a href="#">Gift</a><a href="#">Blog</a><a href="#" style="margin-right:0">Contact Us</a>
    <div class="nav-icons">
      <svg width="16" height="16" viewBox="0 0 24 24" fill="none" stroke="#fff" stroke-width="2"><circle cx="10" cy="10" r="7"/><path d="M15 15l6 6"/></svg>
      <svg width="16" height="16" viewBox="0 0 24 24" fill="none" stroke="#fff" stroke-width="2"><circle cx="12" cy="8" r="4"/><path d="M4 21c1-5 15-5 16 0"/></svg>
      <svg width="16" height="16" viewBox="0 0 24 24" fill="none" stroke="#fff" stroke-width="2"><path d="M5 8h14l-1 13H6z"/><path d="M9 8a3 3 0 0 1 6 0"/></svg>
    </div>
  </nav>
  <h1 class="abs">Discover Your Best<br>Coffee</h1>
  <p class="abs">Lorem ipsum is simply dummy text of the printing and typesetting industry. Lorem ipsum has been the industry's standard dummy text ever since the 1500s.</p>
  <span class="btn abs">Shop Now</span>
  <svg class="tear abs" style="top:800px" height="80" viewBox="0 0 1200 80" preserveAspectRatio="none"><path d="M0 40 L60 30 L110 48 L170 22 L230 44 L300 28 L360 50 L430 26 L500 46 L560 30 L630 52 L700 24 L770 46 L840 28 L910 50 L980 26 L1050 44 L1120 30 L1200 46 L1200 80 L0 80Z" fill="#fff"/></svg>
</section>

<h2 class="section-title abs" style="top:885px">About us</h2>
<div class="title-rule abs" style="top:942px"></div>
<p class="about-text abs">Lorem ipsum is simply dummy text of the printing and typesetting industry. Lorem ipsum has been the industry's standard dummy text ever since the 1500s, when an unknown printer took a galley of type and scrambled it to make a type specimen book. It has survived not only five centuries, but also the leap into electronic typesetting, remaining essentially unchanged. It was popularised in the 1960s with the release of sheets containing passages, and more recently with desktop publishing software like page makers including versions of this text.</p>
<span class="btn abs" style="top:1160px;left:548px">Read More</span>

<h2 class="section-title abs" style="top:1405px">How Subscription works</h2>
<div class="title-rule abs" style="top:1466px"></div>

<div class="step abs" style="left:110px">
  <svg width="56" height="56" viewBox="0 0 48 48" fill="none" stroke="#1c1a19" stroke-width="2"><rect x="10" y="8" width="24" height="32" rx="2"/><path d="M15 16h14M15 22h14M15 28h8"/><path d="M30 34l12-14 3 3-12 14-4 1z"/></svg>
  <h3>You Sign up</h3><div class="rule"></div>
  <p>Lorem ipsum is simply dummy text of the printing and typesetting industry. Lorem ipsum has been the industry's standard dummy text ever since the 1500s.</p>
</div>
<div class="step abs" style="left:445px">
  <svg width="56" height="56" viewBox="0 0 48 48" fill="none" stroke="#1c1a19" stroke-width="2"><ellipse cx="24" cy="24" rx="13" ry="18"/><path d="M24 6c-6 8 6 28 0 36"/></svg>
  <h3>Discover new<br>coffees every Month</h3><div class="rule"></div>
  <p>Lorem ipsum is simply dummy text of the printing and typesetting industry. Lorem ipsum has been the industry's standard dummy text ever since the 1500s.</p>
</div>
<div class="step abs" style="left:780px">
  <svg width="56" height="56" viewBox="0 0 48 48" fill="none" stroke="#1c1a19" stroke-width="2"><path d="M14 12h20l2 30H12z"/><path d="M16 6h16v6H16z"/><circle cx="24" cy="26" r="5"/></svg>
  <h3>Receive monthly pakage<br>of coffee that you love</h3><div class="rule"></div>
  <p>Lorem ipsum is simply dummy text of the printing and typesetting industry. Lorem ipsum has been the industry's standard dummy text ever since the 1500s.</p>
</div>

<h2 class="section-title abs" style="top:2135px">Our Products</h2>
<div class="title-rule abs" style="top:2196px"></div>
<div class="product abs" style="left:110px"><div class="shot"><div class="bag" role="img" aria-label="Blue coffee bag" style="background:linear-gradient(90deg,#1b4f7a,#2a75a8 50%,#1b4f7a)"></div></div><h4>Product Discription</h4><span>$19.95</span></div>
<div class="product abs" style="left:450px"><div class="shot"><div class="bag" role="img" aria-label="Gold coffee bag" style="width:130px;background:linear-gradient(90deg,#b89a5c,#dcc38f 50%,#b89a5c)"></div></div><h4>Product Discription</h4><span>$19.95</span></div>
<div class="product abs" style="left:790px"><div class="shot"><div class="bag" role="img" aria-label="White and brown coffee bag" style="background:linear-gradient(#f2efeb,#c8a98a)"></div></div><h4>Product Discription</h4><span>$19.95</span></div>

<section class="banner abs" role="img" aria-label="Photo of a coffee cup on a wooden table with a sack of roasted beans">
  <svg class="tear abs" style="top:-2px" height="40" viewBox="0 0 1200 40" preserveAspectRatio="none"><path d="M0 0H1200V14L1130 26 1060 10 990 24 920 8 850 28 780 12 700 26 620 10 540 24 460 8 380 26 300 12 220 28 140 10 70 24 0 12Z" fill="#fff"/></svg>
  <h2 class="abs">Design Your Personalized<br>Coffee Subscription</h2>
  <p class="abs">30% off your first box</p>
  <span class="btn abs">Get Started</span>
  <svg class="tear abs" style="top:440px" height="42" viewBox="0 0 1200 42" preserveAspectRatio="none"><path d="M0 20L70 8 140 26 220 10 300 28 380 12 460 30 540 14 620 28 700 10 780 26 860 12 940 30 1020 14 1100 28 1200 12V42H0Z" fill="#fff"/></svg>
</section>

<h2 class="section-title abs" style="top:3310px">Our Latest Blogs</h2>
<div class="title-rule abs" style="top:3371px"></div>
<article class="blog abs" style="left:110px"><div class="shot" role="img" aria-label="Photo of hands holding a cup of latte" style="background:linear-gradient(135deg,#5c3a24,#a07850)"></div><div class="body"><h4>Blog Title #</h4><span class="date">OCT 22,2020</span><p>Lorem ipsum is simply dummy text of the printing and typesetting industry. Lorem ipsum has been the industry's standard dummy text ever since the 1500s.</p><span class="more">Read More</span></div></article>
<article class="blog abs" style="left:445px"><div class="shot" role="img" aria-label="Photo of several cups of coffee with latte art" style="background:linear-gradient(135deg,#8c5a3c,#d2b295)"></div><div class="body"><h4>Blog Title #</h4><span class="date">OCT 22,2020</span><p>Lorem ipsum is simply dummy text of the printing and typesetting industry. Lorem ipsum has been the industry's standard dummy text ever since the 1500s.</p><span class="more">Read More</span></div></article>
<article class="blog abs" style="left:780px"><div class="shot" role="img" aria-label="Photo of a green coffee plantation" style="background:linear-gradient(160deg,#7f9478,#3e5a2c)"></div><div class="body"><h4>Blog Title #</h4><span class="date">OCT 22,2020</span><p>Lorem ipsum is simply dummy text of the printing and typesetting industry. Lorem ipsum has been the industry's standard dummy text ever since the 1500s.</p><span class="more">Read More</span></div></article>
<span class="btn abs" style="top:3936px;left:546px">View More</span>

<div class="partner abs" style="left:100px"></div>
<div class="partner abs" style="left:310px"></div>
<div class="partner abs" style="left:520px"></div>
<div class="partner abs" style="left:730px"></div>
<div class="partner abs" style="left:940px"></div>

<footer class="footer abs">
  <svg class="tear abs" style="top:-30px" height="70" viewBox="0 0 1200 70" preserveAspectRatio="none"><path d="M0 30L60 14 130 36 200 10 270 38 340 16 420 40 500 12 580 36 660 14 740 40 820 10 900 36 980 16 1060 38 1140 12 1200 30V70H0Z" fill="#141211"/></svg>
  <div class="foot-logo abs">Mesa Brew<br>Circle</div>
  <p class="foot-about abs">Lorem ipsum is simply dummy text of the printing and typesetting industry. Lorem ipsum has been the industry's standard dummy text ever since the 1500s.</p>
  <span class="foot-read abs">READ MORE</span>
  <div class="signup abs"><span class="field">EMAIL</span><span class="btn">Subscribe</span></div>

  <h3 class="foot-h abs" style="top:262px;left:600px">Quick Links</h3>
  <ul class="foot-list abs" style="top:330px;left:600px;list-style:none">
    <li>Home</li><li>About us</li><li>Shop</li><li>Subscribe</li><li>Gift</li><li>Blog</li><li>Contact us</li>
  </ul>

  <h3 class="foot-h abs" style="top:262px;left:900px">Contact us</h3>
  <div class="foot-list abs" style="top:330px;left:900px;width:240px">
    <p>Phone: (+00) 012 345 6789</p><p>Fax: (+00) 012 345 6789</p><br>
    <p>E-mail: hello@mesabrewcircle.example</p><br>
    <p>Address: 48 Kiln Row, Harrowdale</p>
  </div>

  <p class="copy abs">Copyright ©2020 mesa brew circle All Rights Reserved.</p>
  <div class="social abs"><i></i><i></i><i></i><i></i><i></i></div>
</footer>

</body>
</html>
```